Buiilding & Construction WebSite

Build a website for the domain www.talbrookhg.com.au
Talbrook Housing Group Pty Ltd of Australia

Please review the docx file I have attached, It shows the web sites I like.
Pls ignore the Designers and Freight Forwarders Sections.

Target Market(s)

Consumers building houses, renovating or upgrading. People building pools, people wanting new kitchens

Industry/Entity Type

Residential Construction

Coding

Coded - Design and coding required

Number of Pages Required

5+ page

Colors

Designer to choose colors to be used in the design.

Requirements
Must have
• Uniqueness
Should not have
• Old styling

```html
<!DOCTYPE html>
<html lang="en">
<head>
<meta charset="utf-8">
<title>Talbrook Housing Group</title>
<link href="https://fonts.googleapis.com/css2?family=Open+Sans:ital,wght@0,400;0,600;0,700;1,600;1,700&family=Roboto:wght@300;400;500;700&display=swap" rel="stylesheet">
<style>
:root{
  --navy:#1b1f5c;
  --navy-deep:#14174a;
  --royal:#2c3a96;
  --sky:#1e8fe0;
  --ink:#222;
  --muted:#555;
  --line:#cfd3e0;
  --paper:#ffffff;
  --mist:#ececef;
}
*{margin:0;padding:0;box-sizing:border-box}
html,body{width:1200px;height:4016px;overflow:hidden}
body{position:relative;font-family:'Roboto',sans-serif;color:var(--ink);background:var(--paper)}
.abs{position:absolute}
.photo{position:absolute}

/* Hero */
.hero{left:0;top:0;width:1200px;height:620px;overflow:hidden}
.hero-photo{inset:0;background:linear-gradient(180deg,#3b4676 0%,#56648f 45%,#6f7ea6 75%,#9aa6c2 100%)}
.hero-shade{position:absolute;inset:0;background:linear-gradient(90deg,rgba(20,23,74,.75) 0%,rgba(20,23,74,.35) 60%,rgba(20,23,74,.2) 100%)}
.brand{left:20px;top:36px;display:flex;align-items:center;gap:12px}
.brand-mark{width:44px;height:44px;border:3px solid #fff}
.brand-name{font-family:'Open Sans',sans-serif;font-weight:700;font-size:15px;color:#fff;line-height:1.15;letter-spacing:.5px;text-transform:uppercase}
.topbar{right:40px;top:14px;color:#fff;font-size:17px}
.nav{right:24px;top:70px;display:flex;gap:34px}
.nav a{color:#fff;text-decoration:none;font-size:26px;font-weight:400}
.nav a.active{border-bottom:2px solid #fff;padding-bottom:4px}
.hero-kicker{left:146px;top:186px;color:#fff;font-size:36px;letter-spacing:1.5px}
.hero-title{left:146px;top:250px;color:#fff;font-size:60px;font-weight:400;line-height:1.15;letter-spacing:1px}
.btn-light{left:146px;top:440px;width:174px;height:42px;border-radius:21px;background:#fff;color:var(--navy);font-size:18px;display:flex;align-items:center;justify-content:center}

/* Welcome */
.welcome{left:0;top:620px;width:1200px;height:540px;overflow:hidden}
.welcome-photo{inset:0;background:linear-gradient(180deg,#b9cde4 0%,#d7e1ea 40%,#c7c1ae 75%,#6f7b55 100%)}
.welcome-title{left:50px;top:905px;width:520px;transform:rotate(-28deg);transform-origin:left bottom;font-family:'Open Sans',sans-serif;font-style:italic;font-weight:700;color:var(--royal);line-height:1.1;white-space:nowrap}
.welcome-title .l1{font-size:46px;display:block;padding-left:40px}
.welcome-title .l2{font-size:38px;display:block}
.welcome-card{left:580px;top:720px;width:560px;height:300px;background:#fff;padding:28px 20px;font-size:13.5px;line-height:1.5;color:var(--muted)}
.welcome-card p+p{margin-top:12px}
.welcome-card a{color:var(--sky);text-decoration:none}
.btn-blue{left:350px;top:950px;width:170px;height:34px;border-radius:17px;background:var(--sky);color:#fff;font-size:15px;display:flex;align-items:center;justify-content:center}

/* Latest project */
.latest{left:0;top:1160px;width:1200px;height:660px}
.thumb{position:absolute;width:328px}
.thumb .pic{height:210px;border:3px solid #fff}
.thumb .cap{height:44px;background:#fff;display:flex;align-items:center;justify-content:space-between;padding:0 12px;font-size:15px;color:var(--navy-deep)}
.arrow-dot{width:22px;height:22px;border-radius:50%;background:var(--navy)}
.latest-title{left:88px;top:1600px;color:#fff;font-family:'Open Sans',sans-serif;font-style:italic;font-weight:700;font-size:46px}
.latest-text{left:88px;top:1668px;width:640px;color:#fff;font-size:19px;line-height:1.5}
.btn-ghost{left:88px;top:1730px;width:150px;height:40px;border:2px solid #fff;border-radius:20px;color:#fff;font-size:15px;letter-spacing:1.5px;display:flex;align-items:center;justify-content:center;background:rgba(255,255,255,.1)}

/* Complete project */
.complete-title{left:0;top:1920px;width:1200px;text-align:center;font-family:'Open Sans',sans-serif;font-style:italic;font-weight:700;font-size:68px;color:var(--royal)}
.done{position:absolute;width:306px}
.done .pic{height:180px}
.done .cap{margin-top:12px;text-align:center;font-size:15px;color:#333}
.btn-outline{left:528px;top:2284px;width:256px;height:52px;border:1px solid #888;color:var(--royal);font-size:12px;letter-spacing:1px;font-weight:500;display:flex;align-items:center;justify-content:center}

/* Testimonial */
.praise-title{left:0;top:2484px;width:1200px;text-align:center;color:#fff;font-family:'Open Sans',sans-serif;font-style:italic;font-weight:600;font-size:50px;line-height:1.4}
.praise-box{left:120px;top:2700px;width:960px;height:320px;border:2px solid #9aa0b8;background:#fff;text-align:center;padding:24px 70px}
.praise-box p{font-size:16px;line-height:1.75;color:#333;margin-top:20px}

/* Contact */
.contact-form{left:88px;top:3140px;width:512px;height:600px;background:var(--navy);padding:34px 50px}
.contact-form h3{color:#fff;font-size:30px;font-weight:700;margin-bottom:26px}
.field{height:42px;border:1px solid #fff;color:#fff;font-size:13px;font-weight:500;padding:0 10px;display:flex;align-items:center;margin-bottom:20px;width:360px}
.field.tall{height:90px;align-items:flex-start;padding-top:10px}
.submit{width:196px;height:44px;background:#fff;color:var(--navy);font-size:20px;display:flex;align-items:center;padding-left:16px;margin-top:2px}
.contact-info{left:600px;top:3140px;width:512px;height:600px;border:1px solid var(--line);border-left:none;text-align:center;padding:34px 40px;color:#333}
.contact-info h3{color:var(--royal);font-size:32px;font-weight:700;margin-bottom:10px}
.contact-info .intro{font-size:13.5px;line-height:1.45;color:var(--muted)}
.contact-info h4{font-size:20px;font-weight:400;margin-top:22px}
.contact-info .val{font-size:18px;line-height:1.4;color:#444}
.contact-info .phones{font-size:18px;font-weight:700;margin-top:22px;line-height:1.5}

/* Footer */
.footer{left:0;top:3752px;width:1200px;height:264px;background:var(--mist)}
.footer-bar{left:88px;top:3832px;width:1024px;height:128px;background:#fff;display:flex;align-items:center;justify-content:space-between;padding:0 28px}
.footer-bar .copy{font-size:16px;color:#333}
.footer-brand{display:flex;align-items:center;gap:10px}
.footer-brand .brand-mark{border-color:var(--navy);width:36px;height:36px}
.footer-brand .brand-name{color:var(--navy);font-size:13px}
.follow{display:flex;align-items:center;gap:14px;font-size:20px;color:#333}
.follow .sep{width:1px;height:60px;background:var(--line);margin-right:10px}
.social{width:44px;height:44px;border:2px solid #333;border-radius:50%}
</style>
</head>
<body>

<!-- Hero -->
<section class="hero abs">
  <div class="photo hero-photo" role="img" aria-label="Modern multi-storey apartment building against the sky"></div>
  <div class="hero-shade"></div>
  <div class="brand abs"><span class="brand-mark"></span><span class="brand-name">Talbrook<br>Housing Group</span></div>
  <div class="topbar abs">Email : info@talbrookhg.com.au &nbsp; Call Us : (+61) 1234567890</div>
  <nav class="nav abs"><a class="active">Home</a><a>About Us</a><a>Services</a><a>Portfolio</a><a>Contact Us</a></nav>
  <div class="hero-kicker abs">Trust Excellence Result</div>
  <h1 class="hero-title abs">Largest Home<br>Biulder</h1>
  <div class="btn-light abs">Explore More</div>
</section>

<!-- Welcome -->
<section class="welcome abs">
  <div class="photo welcome-photo" role="img" aria-label="Large family home with lawn and garden"></div>
  <svg class="abs" style="left:0;top:0" width="1200" height="540" viewBox="0 0 1200 540">
    <polygon points="0,0 1200,0 1200,10 560,10 560,330 0,470" fill="#ffffff"/>
  </svg>
</section>
<div class="welcome-title abs"><span class="l1">Welcome to</span><span class="l2">Talbrook Housing Group</span></div>
<div class="welcome-card abs">
  <p>Lorem ipsum dolor sit amet, consectetur adipiscing elit. Sed iaculis rutrum lorem, et facilisis nibh blandit sed. Maecenas at sodales elit. Phasellus blandit nulla a sagittis euismod. Nulla elementum magna massa, ut egestas est tristique vel. Etiam in finibus sapien. In at hendrerit tellus. Ut a consectetur risus. Donec luctus urna eget dapibus malesuada. Suspendisse lacinia enim augue, id posuere diam placerat vel. Vivamus in aliquam dolor.</p>
  <p>Orci varius natoque penatibus et magnis dis parturient montes, nascetur ridiculus mus. Sed diam risus, rutrum quis volutpat quis, vulputate ac arcu. Aenean venenatis felis enim, quis pretium leo hendrerit nec. Class aptent taciti sociosqu ad litora torquent per conubia nostra, per inceptos himenaeos. <a>Read More</a></p>
</div>
<div class="btn-blue abs">Contact Us</div>

<!-- Latest project -->
<section class="latest abs">
  <svg class="abs" style="left:0;top:0" width="1200" height="660" viewBox="0 0 1200 660">
    <rect width="1200" height="660" fill="#1b1f5c"/>
    <polygon points="0,0 560,0 0,160" fill="#2a2f73"/>
    <polygon points="1200,120 1200,660 620,660" fill="#2c3a96" opacity=".7"/>
    <polygon points="0,660 700,660 0,360" fill="#14174a" opacity=".6"/>
  </svg>
</section>
<div class="thumb" style="left:88px;top:1240px"><div class="pic" role="img" aria-label="Two-storey residential house with front lawn" style="background:linear-gradient(180deg,#8fb0d8,#c9c3b4 60%,#6c7a4e)"></div><div class="cap">View Our Residential Property<span class="arrow-dot"></span></div></div>
<div class="thumb" style="left:436px;top:1240px"><div class="pic" role="img" aria-label="Mediterranean style family home" style="background:linear-gradient(180deg,#9ec0e0,#c89a78 55%,#5f7046)"></div><div class="cap">View Our Residential Property<span class="arrow-dot"></span></div></div>
<div class="thumb" style="left:784px;top:1240px"><div class="pic" role="img" aria-label="Terracotta villa with landscaped garden" style="background:linear-gradient(180deg,#7fa7d4,#b88a62 55%,#4f6a3c)"></div><div class="cap">View Our Residential Property<span class="arrow-dot"></span></div></div>
<h2 class="latest-title abs">Latest Project</h2>
<p class="latest-text abs">Lorem ipsum dolor sit amet, consectetur adipiscing elit. Nam placerat dolor quam, in rhoncus nunc commodo molestie.</p>
<div class="btn-ghost abs">VIEW ALL</div>

<!-- Complete project -->
<h2 class="complete-title abs">Complete Project</h2>
<div class="done" style="left:88px;top:2040px"><div class="pic" role="img" aria-label="Completed modern house at dusk" style="background:linear-gradient(180deg,#6d8fbf,#a7b3c4 60%,#4d5d44)"></div><div class="cap">1107 Harbour Crest Drive - Ashby Vale</div></div>
<div class="done" style="left:448px;top:2040px"><div class="pic" role="img" aria-label="Completed two-storey home with blue sky" style="background:linear-gradient(180deg,#5f8fd0,#b7c3cf 60%,#5b6e48)"></div><div class="cap">2013 Harbour Crest Drive - Ashby Vale</div></div>
<div class="done" style="left:800px;top:2040px"><div class="pic" role="img" aria-label="Completed contemporary house with garden" style="background:linear-gradient(180deg,#5a86c8,#c1c6c9 60%,#566c45)"></div><div class="cap">2005 Wattle Grove Drive - Ashby Vale</div></div>
<div class="btn-outline abs">VIEW ALL PROPERTIES</div>

<!-- Testimonial -->
<svg class="abs" style="left:0;top:2440px" width="1200" height="320" viewBox="0 0 1200 320">
  <polygon points="0,0 1200,0 1200,130 600,300 0,130" fill="#1b1f5c"/>
  <polygon points="0,0 600,0 0,130" fill="#2c3a96" opacity=".6"/>
</svg>
<h2 class="praise-title abs">We Were Thoroughly<br>Impressed</h2>
<div class="praise-box abs">
  <svg width="44" height="36" viewBox="0 0 44 36"><path d="M2 34V20C2 10 8 3 18 2v6c-5 1-8 4-8 10h8v16zM26 34V20c0-10 6-17 16-18v6c-5 1-8 4-8 10h8v16z" fill="#1e8fe0"/></svg>
  <p>Lorem ipsum dolor sit amet, consectetur adipiscing elit. Integer laoreet diam sed euismod dignissim. Proin ante mauris, lobortis vitae egestas et, vestibulum a mi. Vivamus quis ullamcorper urna. Aenean quam ligula, commodo eget dignissim iaculis, condimentum a nunc. Proin consequat ornare pharetra. Pellentesque vitae pellentesque quam, non fermentum nisi. Nam interdum dapibus magna quis vehicula.</p>
</div>

<!-- Contact -->
<div class="contact-form abs">
  <h3>Contact Us</h3>
  <div class="field">Your Name</div>
  <div class="field">Your Email</div>
  <div class="field">Phone No.</div>
  <div class="field tall">Message</div>
  <div class="submit">Submit</div>
</div>
<div class="contact-info abs">
  <h3>Contact Info</h3>
  <p class="intro">Lorem ipsum dolor sit amet, consectetur adipiscing elit. In tincidunt ipsum odio, eu lobortis erat aliquet vitae. Maecenas turpis leo, molestie eu, tempor convallis quam. Quisque mattis placerat vehicula.</p>
  <h4>Address</h4>
  <p class="val">Address Line Street, Zip Code<br>Australia</p>
  <h4>Email</h4>
  <p class="val">info@talbrookhg.com.au<br>contact@talbrookhg.com.au</p>
  <p class="phones">Phone : +12345 67890<br>Fax : +12345 67890</p>
</div>

<!-- Footer -->
<footer class="footer abs"></footer>
<div class="footer-bar abs">
  <span class="copy">2017 talbrookhg.com.au All Right Reserved</span>
  <div class="footer-brand"><span class="brand-mark"></span><span class="brand-name">Talbrook<br>Housing Group</span></div>
  <div class="follow"><span class="sep"></span>Follow Us On <span class="social"></span><span class="social"></span><span class="social"></span></div>
</div>

</body>
</html>
```